Modern Label for cleaning products for the brand Voralux

We need a label design for our line of cleaning products. The label should feature our logo and an image to identify the product's intended use. I've added our logo and an image for use. This only concerns the design of the label on the front of the bottle.

Label dimensions:
Label 1 (500ml bottle with spray): width 58mm x height 115mm
Label 2: (1L bottle): width 73mm x height 140mm
The design must be consistent for both bottles which you find in the pictures.

The bottles to be labeled are white. See the attachment for a photo of the bottles.

The photo must also appear on the label to identify the product's intended use.

Product information:
Brand: Voralux
Product: Sanitary Cleaner

This text must be placed on the label:
"Cleans, descales & freshens. followed with this text: "Ideal for quick and powerful cleaning. A ready-to-use product for everyday use."

- Mention the seperate USP's: Sanitary, Bathroom, Toilet, Wet areas

Appearance: This is a consumer product, but it must have a professional appearance. We would like to see a design that use the color blue from our logo.

Target Market(s)

Consumers who take care of their homes and want to maintain it the correct (professional) way

Font styles to use
Sans Serif

Colors
0054AA
0677BA
7BADD7
CADEEF
E8F1F8

Requirements
Must have
• USP's + use of image and logo + blend in 1 design
Nice to have
• Keep the color of the logo in the design
Should not have
• Comic sans

```html
<!DOCTYPE html>
<html lang="en">
<head>
<meta charset="utf-8">
<title>Voralux Sanitary Cleaner – Front Label</title>
<link rel="stylesheet" href="https://fonts.googleapis.com/css2?family=Montserrat:ital,wght@0,600;0,800;1,700&family=Signika:wght@400;500&display=swap">
<style>
  :root {
    --navy: #1d2f7a;
    --brand-blue: #0054aa;
    --band-blue: #1a4f93;
    --sky: #0677ba;
    --light-blue: #7badd7;
    --ice: #e8f1f8;
    --green: #7cc242;
    --silver-dark: #a9abb0;
    --silver-light: #f4f4f5;
    --ink: #2b2d33;
    --page: #e4e6e9;
    --label-top: #f1f2f4;
  }
  * { margin: 0; padding: 0; box-sizing: border-box; }
  html, body { width: 900px; height: 1200px; overflow: hidden; }
  body {
    background: var(--page);
    font-family: "Signika", sans-serif;
    position: relative;
  }
  .label {
    position: absolute;
    left: 167px;
    top: 40px;
    width: 565px;
    height: 1120px;
    border-radius: 18px;
    overflow: hidden;
    background: linear-gradient(180deg, #ffffff 0%, var(--label-top) 100%);
  }
  .label-art { position: absolute; inset: 0; }
  .brand {
    position: absolute;
    top: 40px;
    left: 24px;
    width: 200px;
    display: flex;
    flex-direction: column;
    align-items: center;
    gap: 10px;
  }
  .brand-dot {
    width: 60px; height: 60px;
    border-radius: 50%;
    background: var(--brand-blue);
  }
  .brand-name {
    font-family: "Montserrat", sans-serif;
    font-weight: 600;
    font-size: 32px;
    color: var(--ink);
    letter-spacing: 0.5px;
  }
  .product-title {
    position: absolute;
    top: 240px;
    left: 92px;
    width: 420px;
    text-align: center;
  }
  .product-name {
    font-family: "Montserrat", sans-serif;
    font-weight: 800;
    font-size: 80px;
    line-height: 1;
    color: var(--navy);
    letter-spacing: -2px;
  }
  .product-type {
    font-family: "Montserrat", sans-serif;
    font-weight: 600;
    font-size: 28px;
    letter-spacing: 18px;
    color: var(--ink);
    margin-top: 2px;
    padding-left: 18px;
  }
  .benefits {
    font-family: "Montserrat", sans-serif;
    font-weight: 700;
    font-style: italic;
    font-size: 31px;
    fill: #ffffff;
  }
  .surfaces {
    position: absolute;
    top: 506px;
    left: 0;
    width: 565px;
    text-align: center;
    font-size: 33px;
    line-height: 42px;
    letter-spacing: 1px;
    color: var(--ink);
  }
  .usage {
    position: absolute;
    top: 633px;
    left: 0;
    width: 565px;
    text-align: center;
    font-size: 31px;
    line-height: 41px;
    letter-spacing: 1px;
    color: #ffffff;
  }
</style>
</head>
<body>
  <div class="label">
    <svg class="label-art" width="565" height="1120" viewBox="0 0 565 1120">
      <defs>
        <linearGradient id="silver" x1="0" y1="0" x2="1" y2="0">
          <stop offset="0" stop-color="var(--silver-dark)"/>
          <stop offset="0.5" stop-color="var(--silver-light)"/>
          <stop offset="1" stop-color="var(--silver-dark)"/>
        </linearGradient>
        <linearGradient id="scene-tones" x1="0" y1="0" x2="1" y2="1">
          <stop offset="0" stop-color="#7d8185"/>
          <stop offset="0.45" stop-color="#c9ccd0"/>
          <stop offset="1" stop-color="#8e9194"/>
        </linearGradient>
        <path id="benefit-curve" d="M45,392 Q280,470 545,448"/>
      </defs>

      <!-- green + blue benefit band -->
      <path d="M0,330 Q290,420 565,385 L565,500 L0,500 Z" fill="var(--green)"/>
      <path d="M0,345 Q290,432 565,398 L565,500 L0,500 Z" fill="var(--band-blue)"/>
      <text class="benefits"><textPath href="#benefit-curve">Cleans  |  Descales  |  Freshens</textPath></text>

      <!-- silver surfaces band -->
      <rect x="0" y="492" width="565" height="124" fill="url(#silver)"/>
      <rect x="0" y="492" width="565" height="3" fill="#ffffff"/>
      <rect x="0" y="613" width="565" height="3" fill="#ffffff"/>

      <!-- usage band -->
      <rect x="0" y="616" width="565" height="260" fill="var(--band-blue)"/>

      <!-- green wave above image area -->
      <path d="M0,845 Q280,790 565,865 L565,1120 L0,1120 Z" fill="var(--green)"/>
      <g role="img" aria-label="Photo of a modern bathroom with glass shower, vanity and tiled bath">
        <path d="M0,858 Q280,806 565,878 L565,1120 L0,1120 Z" fill="url(#scene-tones)"/>
      </g>
    </svg>

    <div class="brand">
      <span class="brand-dot"></span>
      <span class="brand-name">voralux</span>
    </div>

    <div class="product-title">
      <div class="product-name">Sanitary</div>
      <div class="product-type">CLEANER</div>
    </div>

    <p class="surfaces">Sanitary, Bathroom, Toilet<br>&amp; Wet areas</p>

    <p class="usage">Ideal For Quick And Powerful<br>Cleaning.<br>A Ready-to-use Product For<br>Everyday Use</p>
  </div>
</body>
</html>
```